Redesign Website - Current one too plain

The description is in the uploaded file. Please let me know if you need any more information. I'd prefer it if someone could implement the design to a WordPress site but the best design will win, regardless.
I would like the forms to look nice as well
UPDATE:
I don't think we can use the images that I provided, I think they make the site look a bit 'cheap' and I really don't know how to replace them. One thought I have had is to make the "Simple, Unique, Effective" a second feature on the right side of the page with the search on the left
Target Market(s)
Small companies, private sellers of cars and people who rent their caravan/holiday home out
Industry/Entity Type
Advertising
Number of Pages Required
3 page
Colors
Designer to choose colors to be used in the design.
Look and feel

```html
<!DOCTYPE html>
<html lang="en">
<head>
<meta charset="utf-8">
<title>Contact Us – Blotra</title>
<link href="https://fonts.googleapis.com/css2?family=Poppins:wght@400;500;600;700&display=swap" rel="stylesheet">
<style>
:root{
  --ink:#2b2b2b;
  --muted:#8d8d8d;
  --accent:#e2ff00;
  --accent-edge:#c9e300;
  --band:#eeeeee;
  --field:#f2f2f2;
  --white:#ffffff;
  --rule:#dcdcdc;
}
*{box-sizing:border-box;margin:0;padding:0}
html,body{width:1200px;height:985px;overflow:hidden}
body{position:relative;background:var(--white);font-family:'Poppins',sans-serif;color:var(--ink)}
.site-header{position:absolute;left:0;top:0;width:1200px;height:101px;background:var(--white)}
.brand{position:absolute;left:89px;top:22px;display:flex;align-items:center;gap:12px}
.brand-dot{width:34px;height:34px;border-radius:50%;background:var(--accent)}
.brand-name{font-weight:600;font-size:31px;letter-spacing:6px;color:var(--ink)}
.main-nav{position:absolute;left:462px;top:30px;display:flex;align-items:center;height:26px}
.nav-item{display:flex;align-items:center;gap:7px;font-size:12.5px;font-weight:500;padding:0 20px;height:26px;color:var(--ink);text-decoration:none}
.nav-item + .nav-item{border-left:1px solid var(--rule)}
.nav-item svg{width:17px;height:17px;fill:none;stroke:var(--ink);stroke-width:1.6}
.nav-item svg.solid{fill:var(--ink);stroke:none}
.advertise-btn{position:absolute;left:908px;top:23px;width:203px;height:43px;background:var(--accent);border-radius:5px;display:flex;align-items:center;justify-content:center;font-size:12px;font-weight:700;color:var(--ink)}
.hero-band{position:absolute;left:0;top:101px;width:1200px;height:607px;background:var(--band)}
.page-title{position:absolute;left:0;top:166px;width:1200px;text-align:center;font-size:41px;font-weight:700}
.page-lead{position:absolute;left:0;top:225px;width:1200px;text-align:center;font-size:14px}
.contact-card{position:absolute;left:307px;top:284px;width:586px;height:518px;background:var(--white);border-radius:27px;box-shadow:0 30px 80px rgba(0,0,0,.08)}
.field-label{position:absolute;font-size:10.5px;font-weight:500;text-transform:uppercase}
.field-label span{color:var(--accent-edge)}
.field{position:absolute;background:var(--field);border-radius:5px;font-size:12.5px;color:var(--muted);padding:12px 20px}
.counter{position:absolute;right:45px;top:366px;font-size:12.5px;color:var(--muted)}
.submit-btn{position:absolute;left:225px;top:407px;width:136px;height:46px;background:var(--accent);border-radius:5px;box-shadow:0 3px 0 var(--accent-edge);display:flex;align-items:center;justify-content:center;font-size:14px;font-weight:700}
.footer-rule{position:absolute;left:89px;top:917px;width:1022px;height:2px;background:#e4e4e4}
.copyright{position:absolute;left:0;top:937px;width:1200px;text-align:center;font-size:14px;font-weight:500}
.to-top{position:absolute;left:1136px;top:898px;width:40px;height:40px;background:var(--ink);border-radius:4px;display:flex;align-items:center;justify-content:center}
</style>
</head>
<body>
<header class="site-header">
  <div class="brand"><span class="brand-dot"></span><span class="brand-name">BLOTRA</span></div>
  <nav class="main-nav">
    <a class="nav-item"><svg class="solid" viewBox="0 0 24 24"><path d="M12 3 2 12h3v8h5v-5h4v5h5v-8h3z"/></svg>HOME</a>
    <a class="nav-item"><svg viewBox="0 0 24 24"><rect x="5" y="3" width="15" height="18" rx="1"/><circle cx="12.5" cy="10" r="2.5"/><path d="M8.5 17c1-2.5 7-2.5 8 0M3 7h3M3 12h3M3 17h3"/></svg>CONTACT</a>
    <a class="nav-item"><svg viewBox="0 0 24 24"><circle cx="10" cy="7" r="4"/><path d="M3 21c0-5 4-8 8-8M14 20l1-3 5-5 2 2-5 5z"/></svg>REGISTER</a>
    <a class="nav-item"><svg viewBox="0 0 24 24"><circle cx="12" cy="7" r="4"/><path d="M4 21c0-5 4-7 8-7s8 2 8 7z"/></svg>LOGIN</a>
  </nav>
  <div class="advertise-btn">ADVERTISE YOUR COMPANY</div>
</header>

<section class="hero-band"></section>
<h1 class="page-title">Contact Us</h1>
<p class="page-lead">We can help, our team of experts is on hand to answer your questions.</p>

<form class="contact-card">
  <div class="field-label" style="left:44px;top:50px">Name<span>*</span></div>
  <div class="field" style="left:45px;top:70px;width:495px;height:41px">Enter your name</div>
  <div class="field-label" style="left:44px;top:128px">Email<span>*</span></div>
  <div class="field" style="left:45px;top:148px;width:244px;height:41px">Enter your email</div>
  <div class="field-label" style="left:296px;top:128px">Phone<span>*</span></div>
  <div class="field" style="left:297px;top:148px;width:244px;height:41px">Enter your phone number</div>
  <div class="field-label" style="left:44px;top:204px">Message<span>*</span></div>
  <div class="field" style="left:45px;top:224px;width:495px;height:132px">Type your text</div>
  <div class="counter">0 of 4000 max characters</div>
  <div class="submit-btn">SUBMIT</div>
</form>

<div class="footer-rule"></div>
<p class="copyright">© Copyright 2023 Blotra. All Rights Reserved</p>
<div class="to-top"><svg width="10" height="8" viewBox="0 0 10 8"><path d="M2 6 5 3l3 3" fill="none" stroke="#e2ff00" stroke-width="1.6"/></svg></div>
</body>
</html>
```